Company providing wellness products (skin care, herbal, soap) needs website design.

Our Silver Heron Acres is Silver Heron Acres and we provide wellness products for our customers. We also provide organically grown vegetables and herbs. Our website is on Wix and we have the basic layout completed; however, we need a better design. I assume this means that we can import the designs that you provide into the Wix environment. If this is not true, we do not want to move forward with the project. I included a copy of a logo that was done by your team.

Target Market(s)

women with income exceeded 75k interested in health and natural products.

Industry/Entity Type

Skin Care Product

Number of Pages Required

5+ page

Font styles to use
Serif
Sans Serif
Decorative
Script

Requirements
Must have
• Not sure of the number of pages as I really need a theme designed that I can carry throughout the site.
Nice to have
• clean, fresh, organic sophisticated feel. I would like to incorporate our logo that I attached. We are open to a different logo if it works better with your design. Our name is Silver Heron Acres and our logo is green so I think green should be incorporated but are open to what you design.

```html
<!DOCTYPE html>
<html lang="en">
<head>
<meta charset="utf-8">
<title>Silver Heron Acres — Choose Wellness</title>
<link rel="stylesheet" href="https://fonts.googleapis.com/css2?family=Lato:wght@400;700;900&display=swap">
<style>
:root{
  --green:#5a9a2e;
  --green-dark:#4a8524;
  --ink:#1e1e1e;
  --text:#3a3a3a;
  --card:#eeeeee;
  --footer:#f1f1f1;
  --bar:#1c1c1c;
  --star:#f39c12;
  --white:#ffffff;
}
*{margin:0;padding:0;box-sizing:border-box}
html,body{width:1200px;height:3653px;overflow:hidden}
body{position:relative;font-family:"Lato",sans-serif;color:var(--text);background:var(--white)}
.abs{position:absolute}
.btn{position:absolute;display:flex;align-items:center;justify-content:center;background:var(--green);color:var(--white);font-weight:700;font-size:15px;letter-spacing:.3px;text-transform:uppercase}

/* header */
.brand{left:74px;top:0;width:270px;height:160px;display:flex;align-items:center;gap:10px}
.brand-dot{width:34px;height:34px;border-radius:50%;background:var(--green);flex:none}
.brand-name{font-size:24px;font-weight:700;color:var(--green);line-height:1.1}
.call{left:838px;top:36px;display:flex;align-items:center;gap:14px}
.call-icon{width:38px;height:38px;border-radius:50%;background:var(--green);display:flex;align-items:center;justify-content:center}
.call-label{font-size:13px;font-weight:700;color:var(--green);line-height:1}
.call-number{font-size:31px;color:var(--ink);line-height:1.1;margin-top:3px}
.nav{left:300px;top:111px;width:900px;height:49px;background:var(--green);clip-path:polygon(23px 0,100% 0,100% 100%,0 100%)}
.nav a{position:absolute;top:0;line-height:49px;color:var(--white);font-size:14px;text-decoration:none;transform:translateX(-50%);white-space:nowrap}

/* hero */
.hero{left:0;top:160px;width:1200px;height:640px;background:linear-gradient(100deg,#b9b2a6 0%,#d8d4ce 35%,#e9e6e2 60%,#cfc9c1 100%)}
.hero-title{left:75px;top:382px;font-size:50px;font-weight:900;color:var(--white);letter-spacing:.5px}
.hero-sub{left:75px;top:444px;font-size:29px;color:var(--white)}
.dots{left:75px;top:690px;display:flex;gap:8px}
.dots span{width:9px;height:9px;border-radius:50%;background:var(--white)}
.dots span:first-child{background:var(--green)}
.hero-wave{left:0;top:740px;width:1200px;height:60px}

/* welcome */
.welcome-mark{left:100px;top:870px;width:390px;height:414px;display:flex;flex-direction:column;align-items:center;justify-content:center;gap:20px}
.welcome-circle{width:280px;height:280px;border-radius:50%;background:var(--green)}
.welcome-name{font-size:30px;font-weight:700;color:var(--green)}
.section-h{font-size:33px;font-weight:900;color:var(--ink)}
.para{font-size:14.5px;line-height:29.5px;color:var(--text)}

/* bands */
.band{left:0;width:1200px;background:linear-gradient(110deg,#1d1d1b 0%,#2c3a20 30%,#3f6b22 60%,#5d9a2c 100%)}
.band-h{left:0;width:1200px;text-align:center;font-size:33px;color:var(--white);letter-spacing:.5px}
.band-dot{left:587px;width:26px;height:26px;border-radius:50%;border:2px solid var(--white)}
.card{position:absolute;background:var(--card);width:330px}
.photo{position:absolute;border-radius:50%;border:4px solid #4b5e63}
.card-title{position:absolute;left:0;width:100%;text-align:center;font-size:20px;font-weight:700;color:var(--green)}
.card-text{position:absolute;left:30px;width:270px;text-align:center;font-size:14px;line-height:26px;color:var(--text)}
.stars{position:absolute;left:0;width:100%;text-align:center;color:var(--star);font-size:20px;letter-spacing:4px}
.name-h{position:absolute;left:0;width:100%;text-align:center;font-size:15px;font-weight:700;color:var(--green)}

/* footer */
.footer{left:0;top:3270px;width:1200px;height:320px;background:var(--footer)}
.foot-h{font-size:17px;color:var(--green);font-weight:700}
.foot-list{font-size:14px;line-height:27.5px;color:var(--ink);list-style:none}
.foot-contact li{display:flex;align-items:center;gap:12px}
.bar{left:0;top:3590px;width:1200px;height:63px;background:var(--bar)}
.copy{left:75px;top:3613px;font-size:12px;color:#9a9a9a}
.social{left:946px;top:3612px;display:flex;gap:18px}
.social span{width:20px;height:20px;border-radius:50%;background:#b9b9b9}
</style>
</head>
<body>

<header>
  <div class="abs brand"><span class="brand-dot"></span><span class="brand-name">Silver Heron Acres</span></div>
  <div class="abs call">
    <div class="call-icon">
      <svg width="18" height="18" viewBox="0 0 24 24"><path fill="#fff" d="M6.6 10.8a15.1 15.1 0 0 0 6.6 6.6l2.2-2.2a1 1 0 0 1 1-.25 11.4 11.4 0 0 0 3.6.57 1 1 0 0 1 1 1V20a1 1 0 0 1-1 1A17 17 0 0 1 3 4a1 1 0 0 1 1-1h3.5a1 1 0 0 1 1 1c0 1.25.2 2.45.57 3.57a1 1 0 0 1-.25 1z"/></svg>
    </div>
    <div><div class="call-label">CALL US TODAY</div><div class="call-number">1-800-555-0148</div></div>
  </div>
  <nav class="abs nav">
    <a style="left:66px">HOME</a><a style="left:165px">ABOUT US</a><a style="left:281px">PRODUCTS</a><a style="left:395px">SERVICES</a><a style="left:543px">CUSTOMER REVIEWS</a><a style="left:676px">BLOG</a><a style="left:782px">CONTACT US</a>
  </nav>
</header>

<section>
  <div class="abs hero" role="img" aria-label="Photo of a mother and daughter in head towels applying face cream together"></div>
  <div class="abs hero-title">SILVER HERON ACRES</div>
  <div class="abs hero-sub">CHOOSE WELLNESS</div>
  <div class="btn" style="left:75px;top:502px;width:150px;height:41px">Read More</div>
  <div class="abs dots"><span></span><span></span><span></span><span></span></div>
  <svg class="abs hero-wave" viewBox="0 0 1200 60" preserveAspectRatio="none">
    <path d="M0 60 L0 40 C300 0 500 10 700 30 C900 50 1050 40 1200 25 L1200 60 Z" fill="#fff"/>
    <path d="M0 40 C300 0 500 10 700 30 C900 50 1050 40 1200 25 L1200 18 C1050 34 900 42 700 22 C500 2 300 -6 0 34 Z" fill="var(--green)"/>
  </svg>
</section>

<section>
  <div class="abs welcome-mark"><div class="welcome-circle"></div><div class="welcome-name">Silver Heron Acres</div></div>
  <h2 class="abs section-h" style="left:525px;top:902px">WELCOME TO OUR WEBSITE</h2>
  <p class="abs para" style="left:525px;top:959px;width:600px">Sed ut perspiciatis unde omnis iste natus error sit voluptatem accusantium doloremque laudantium, totam rem aperiam, eaque ipsa quae ab illo inventore veritatis et quasi architecto beatae vitae dicta sunt explicabo. Nemo enim ipsam voluptatem quia voluptas sit aspernatur aut odit aut fugit, sed quia consequuntur magni dolores eos qui ratione voluptatem sequi nesciunt. Neque porro quisquam est, qui dolorem ipsum quia dolor sit amet, consectetur, adipisci velit, sed quia non numquam eius modi tempora incidunt ut labore et dolore magnam aliquam quaerat voluptatem.</p>
  <div class="btn" style="left:525px;top:1196px;width:150px;height:41px">Read More</div>
</section>

<section>
  <div class="abs band" style="top:1390px;height:444px"></div>
  <h2 class="abs band-h" style="top:1440px;font-weight:400">WELLNESS PRODUCTS</h2>
  <div class="abs band-dot" style="top:1505px"></div>

  <div class="card" style="left:75px;top:1640px;height:361px">
    <div class="photo" role="img" aria-label="Photo of white skin care bottles on a pink backdrop" style="left:54px;top:-67px;width:222px;height:222px;background:linear-gradient(135deg,#f6c6c6,#e99a9c)"></div>
    <div class="card-title" style="top:178px">SKIN CARE</div>
    <div class="card-text" style="top:204px">Sed viverra ultrices mi vel vehicula. Pellentesque ornare felis nisi, vel malesuada arcu lacinia eu.</div>
    <div class="btn" style="left:61px;top:300px;width:208px;height:39px">Read More</div>
  </div>
  <div class="card" style="left:436px;top:1640px;height:361px">
    <div class="photo" role="img" aria-label="Photo of amber herbal oil bottles with a brush" style="left:54px;top:-67px;width:222px;height:222px;background:linear-gradient(135deg,#e9e4dc,#8a5a34)"></div>
    <div class="card-title" style="top:178px">HERBAL</div>
    <div class="card-text" style="top:204px">Sed viverra ultrices mi vel vehicula. Pellentesque ornare felis nisi, vel malesuada arcu lacinia eu.</div>
    <div class="btn" style="left:61px;top:300px;width:208px;height:39px">Read More</div>
  </div>
  <div class="card" style="left:796px;top:1640px;height:361px">
    <div class="photo" role="img" aria-label="Photo of handmade soap bars with herbs" style="left:54px;top:-67px;width:222px;height:222px;background:linear-gradient(135deg,#a9c98a,#efd9a6)"></div>
    <div class="card-title" style="top:178px">SOAP</div>
    <div class="card-text" style="top:204px">Sed viverra ultrices mi vel vehicula. Pellentesque ornare felis nisi, vel malesuada arcu lacinia eu.</div>
    <div class="btn" style="left:61px;top:300px;width:208px;height:39px">Read More</div>
  </div>
</section>

<section>
  <h2 class="abs section-h" style="left:75px;top:2137px">OUR SERVICES</h2>
  <p class="abs para" style="left:75px;top:2193px;width:600px">Sed ut perspiciatis unde omnis iste natus error sit voluptatem accusantium doloremque laudantium, totam rem aperiam, eaque ipsa quae ab illo inventore veritatis et quasi architecto beatae vitae dicta sunt explicabo. Nemo enim ipsam voluptatem quia voluptas sit aspernatur aut odit aut fugit, sed quia consequuntur magni dolores eos qui ratione voluptatem sequi nesciunt. Neque porro quisquam est, qui dolorem ipsum quia dolor sit amet, consectetur, adipisci velit, sed quia non numquam eius modi tempora incidunt ut labore et dolore magnam aliquam quaerat voluptatem.</p>
  <div class="btn" style="left:75px;top:2431px;width:150px;height:41px">Read More</div>
  <div class="abs" role="img" aria-label="Photo of cosmetic creams, clay masks, oil and roses on a grey surface" style="left:705px;top:2099px;width:420px;height:420px;border-radius:50%;background:radial-gradient(circle at 55% 50%,#b7c4c0 0%,#9aa3a2 55%,#7f8886 100%)"></div>
</section>

<section>
  <div class="abs band" style="top:2597px;height:444px"></div>
  <h2 class="abs band-h" style="top:2648px;font-weight:400">CUSTOMER TESTIMONIALS</h2>
  <div class="abs band-dot" style="top:2713px"></div>

  <div class="card" style="left:75px;top:2851px;height:329px">
    <div class="photo" role="img" aria-label="Portrait photo of a customer" style="left:91px;top:-77px;width:148px;height:148px;border:4px solid #fff;background:linear-gradient(160deg,#d9d4cf,#b89a7a)"></div>
    <div class="stars" style="top:97px">★★★★★</div>
    <div class="card-text" style="top:131px;line-height:27.7px;left:20px;width:290px">“ Sed ut perspiciatis unde omnis iste natus error sit voluptatem accusantium doloremque laudantium, totam rem aperiam, eaque ipsa quae ab illo inventore veritatis et quasi&nbsp; architecto..”</div>
    <div class="name-h" style="top:280px">NAME HEADING</div>
  </div>
  <div class="card" style="left:436px;top:2851px;height:329px">
    <div class="photo" role="img" aria-label="Portrait photo of a customer" style="left:91px;top:-77px;width:148px;height:148px;border:4px solid #fff;background:linear-gradient(160deg,#eee8dd,#d8b98a)"></div>
    <div class="stars" style="top:97px">★★★★★</div>
    <div class="card-text" style="top:131px;line-height:27.7px;left:20px;width:290px">“ Sed ut perspiciatis unde omnis iste natus error sit voluptatem accusantium doloremque laudantium, totam rem aperiam, eaque ipsa quae ab illo inventore veritatis et quasi&nbsp; architecto..”</div>
    <div class="name-h" style="top:280px">NAME HEADING</div>
  </div>
  <div class="card" style="left:796px;top:2851px;height:329px">
    <div class="photo" role="img" aria-label="Portrait photo of a customer" style="left:91px;top:-77px;width:148px;height:148px;border:4px solid #fff;background:linear-gradient(160deg,#e4e4e4,#6b4a3a)"></div>
    <div class="stars" style="top:97px">★★★★★</div>
    <div class="card-text" style="top:131px;line-height:27.7px;left:20px;width:290px">“ Sed ut perspiciatis unde omnis iste natus error sit voluptatem accusantium doloremque laudantium, totam rem aperiam, eaque ipsa quae ab illo inventore veritatis et quasi&nbsp; architecto..”</div>
    <div class="name-h" style="top:280px">NAME HEADING</div>
  </div>
</section>

<footer>
  <div class="abs footer"></div>
  <svg class="abs" style="left:0;top:3250px" width="1200" height="60" viewBox="0 0 1200 60" preserveAspectRatio="none">
    <path d="M0 60 L0 45 C250 15 500 15 750 30 C950 42 1100 28 1200 12 L1200 60 Z" fill="var(--footer)"/>
    <path d="M0 45 C250 15 500 15 750 30 C950 42 1100 28 1200 12 L1200 4 C1100 22 950 36 750 22 C500 8 250 8 0 40 Z" fill="var(--green)"/>
  </svg>
  <div class="abs brand" style="top:3395px;height:140px"><span class="brand-dot"></span><span class="brand-name">Silver Heron Acres</span></div>

  <div class="abs" style="left:328px;top:3366px">
    <div class="foot-h">SITE MAP</div>
    <ul class="foot-list" style="margin-top:2px"><li>Home</li><li>About Us</li><li>Products</li><li>Services</li></ul>
  </div>
  <ul class="abs foot-list" style="left:461px;top:3392px"><li>Customer Reviews</li><li>Blog</li><li>Contact Us</li></ul>

  <div class="abs" style="left:677px;top:3366px">
    <div class="foot-h">RESOURSES</div>
    <ul class="foot-list" style="margin-top:2px"><li>Lorem ipsum dolor</li><li>Sit amet</li><li>Consectetur</li><li>Adipiscing elit</li><li>Duntabore</li></ul>
  </div>

  <div class="abs" style="left:909px;top:3366px">
    <div class="foot-h">CONTACT INFO</div>
    <div class="foot-list" style="margin-top:4px;line-height:24px">4120 Willow Bend<br>Road, Ashford, KT7 3LQ</div>
    <ul class="foot-list foot-contact" style="line-height:25px;margin-top:4px">
      <li><svg width="12" height="12" viewBox="0 0 24 24"><path fill="#222" d="M6.6 10.8a15.1 15.1 0 0 0 6.6 6.6l2.2-2.2a1 1 0 0 1 1-.25 11.4 11.4 0 0 0 3.6.57 1 1 0 0 1 1 1V20a1 1 0 0 1-1 1A17 17 0 0 1 3 4a1 1 0 0 1 1-1h3.5a1 1 0 0 1 1 1c0 1.25.2 2.45.57 3.57a1 1 0 0 1-.25 1z"/></svg><span style="margin-left:9px">1-800-555-0148</span></li>
      <li><svg width="13" height="10" viewBox="0 0 26 20"><path fill="#222" d="M0 0h26v3L13 11 0 3zM0 6l13 8 13-8v14H0z"/></svg><span style="margin-left:8px">hello@silverheronacres.com</span></li>
      <li><svg width="11" height="14" viewBox="0 0 22 28"><path fill="#222" d="M11 0a11 11 0 0 1 11 11c0 8-11 17-11 17S0 19 0 11A11 11 0 0 1 11 0zm0 6a5 5 0 1 0 0 10 5 5 0 0 0 0-10z"/></svg><span style="margin-left:10px">Map Location</span></li>
    </ul>
  </div>

  <div class="abs bar"></div>
  <div class="abs copy">Copyright © 2021 Silver Heron Acres All rights reserved.</div>
  <div class="abs social"><span></span><span></span><span></span><span></span><span></span></div>
</footer>

</body>
</html>
```